Halvern Power "Unique Process" Graphic

Create a "graphic" that creatively represents the seven-step process that Halvern Power uses to serve our customers.
This graphic should be sized in such a way that it can easily be included on a page in our website, and also used in other marketing materials such as flyers, emails and powerpoint presentations.
As an EXAMPLE of a similar graphic, see the "Proven Process" section of the home page of this website - https://www.trelvonsite.com/
I'll include our brand documentation as well as the document for our "Unique Process" in the uploaded files section.
Please use our brand colors and also be creative in how you represent the seven steps graphically.
Here's a bit about our business.
Halvern Power is one of the largest B2B Energy Brokers in the US. We serve tens of thousands of customers by securing energy contracts for them. We are NOT an energy company ourselves - but a broker that represents 30+ energy suppliers to commercial and nonprofit customers.

```html
<!DOCTYPE html>
<html lang="en">
<head>
<meta charset="utf-8">
<title>Halvern Power – Unique Process</title>
<link href="https://fonts.googleapis.com/css2?family=Roboto:wght@300;400;700;900&display=swap" rel="stylesheet">
<style>
  :root {
    --navy: #1b3768;
    --green: #0a9a4c;
    --ink: #111111;
    --dash: #8a8d91;
    --paper: #ffffff;
  }
  * { margin: 0; padding: 0; box-sizing: border-box; }
  html, body { width: 1200px; height: 896px; overflow: hidden; background: var(--paper); }
  .process {
    position: relative;
    width: 1200px;
    height: 896px;
    font-family: "Roboto", Arial, sans-serif;
    color: var(--navy);
  }
  .process__art { position: absolute; inset: 0; }
  .process__title {
    position: absolute;
    left: 40px;
    top: 70px;
    font-size: 34px;
    font-weight: 900;
    color: var(--ink);
    letter-spacing: 0.2px;
  }
  .step {
    position: absolute;
    width: 240px;
    transform: translateX(-50%);
    text-align: center;
    font-size: 12.6px;
    font-weight: 300;
    line-height: 16.8px;
  }
  .step__name {
    font-size: 13.2px;
    font-weight: 700;
    line-height: 17px;
  }
  .brand {
    position: absolute;
    left: 850px;
    top: 735px;
    display: flex;
    align-items: center;
    gap: 12px;
  }
  .brand__square { width: 34px; height: 34px; background: var(--green); }
  .brand__name {
    font-size: 32px;
    font-weight: 900;
    color: var(--navy);
    letter-spacing: 0.5px;
  }
</style>
</head>
<body>
<main class="process">
  <svg class="process__art" width="1200" height="896" viewBox="0 0 1200 896" xmlns="http://www.w3.org/2000/svg">
    <defs>
      <marker id="flow-arrow" viewBox="0 0 12 12" refX="6" refY="6" markerWidth="13" markerHeight="13" markerUnits="userSpaceOnUse" orient="auto">
        <path d="M1 2 L11 6 L1 10 L3.5 6 Z" fill="#fff"/>
      </marker>
    </defs>

    <!-- connector lines -->
    <g class="connectors" fill="none" stroke="var(--dash)" stroke-width="3" stroke-dasharray="9 8">
      <path d="M652 113 H720 V134"/>
      <path d="M529 285 H569 V337"/>
      <path d="M232 363 H269 V416"/>
      <path d="M965 292 H1005 V344"/>
      <path d="M801 553 V604 H841"/>
      <path d="M475 635 V690 H516"/>
      <path d="M148 733 V766 H189"/>
    </g>

    <!-- route band -->
    <path class="route" d="M149 684 L269 469 L472 587 L596 379 L801 503 L907 293 L722 182 L596 379"
          fill="none" stroke="var(--navy)" stroke-width="26" stroke-linejoin="round"/>

    <!-- direction arrows -->
    <g class="route-arrows" fill="none" stroke="none" marker-mid="url(#flow-arrow)">
      <path d="M149 684 L185 620 L209 577 L233 533 L269 469"/>
      <path d="M269 469 L330 504 L371 528 L411 552 L472 587"/>
      <path d="M472 587 L509 525 L534 483 L559 441 L596 379"/>
      <path d="M596 379 L658 416 L699 441 L740 466 L801 503"/>
      <path d="M801 503 L833 440 L854 398 L875 356 L907 293"/>
      <path d="M907 293 L852 260 L815 238 L778 215 L722 182"/>
      <path d="M722 182 L684 241 L659 281 L634 321 L596 379"/>
    </g>

    <!-- stations -->
    <g class="stations" fill="var(--paper)" stroke="var(--navy)" stroke-width="5">
      <circle cx="149" cy="684" r="40"/>
      <circle cx="269" cy="469" r="40"/>
      <circle cx="472" cy="587" r="40"/>
      <circle cx="596" cy="379" r="40"/>
      <circle cx="801" cy="503" r="40"/>
      <circle cx="907" cy="293" r="40"/>
      <circle cx="722" cy="182" r="40"/>
    </g>

    <!-- icons -->
    <g class="icons" fill="none" stroke="var(--green)" stroke-width="2" stroke-linecap="round" stroke-linejoin="round">
      <!-- assessment: clipboard tick -->
      <g transform="translate(149 684)">
        <rect x="-16" y="-20" width="28" height="38" rx="3"/>
        <rect x="-8" y="-24" width="12" height="6" rx="2"/>
        <path d="M-10 -10 H6 M-10 -3 H6 M-10 4 H0"/>
        <path d="M-2 10 L4 16 L18 0"/>
      </g>
      <!-- options: choice circles -->
      <g transform="translate(269 469)" font-family="Roboto, Arial, sans-serif" font-size="8" font-weight="700">
        <circle cx="-7" cy="-18" r="6"/><circle cx="7" cy="-18" r="6"/>
        <circle cx="-14" cy="-4" r="6"/><circle cx="14" cy="-4" r="6"/>
        <text x="-7" y="-15" text-anchor="middle" fill="var(--green)" stroke="none">B</text>
        <text x="7" y="-15" text-anchor="middle" fill="var(--green)" stroke="none">C</text>
        <text x="-14" y="-1" text-anchor="middle" fill="var(--green)" stroke="none">A</text>
        <text x="14" y="-1" text-anchor="middle" fill="var(--green)" stroke="none">D</text>
        <path d="M0 2 V22 M-6 8 H6"/>
      </g>
      <!-- sign up: button and pointer -->
      <g transform="translate(472 587)">
        <rect x="-23" y="-15" width="46" height="16" rx="8"/>
        <text x="0" y="-3" text-anchor="middle" font-family="Roboto, Arial, sans-serif" font-size="10" font-weight="700" fill="var(--green)" stroke="none">SIGN UP</text>
        <path d="M-4 22 V4 a2.5 2.5 0 0 1 5 0 V12 M1 10 a2.5 2.5 0 0 1 5 0 V13 M6 11 a2.5 2.5 0 0 1 5 0 V22"/>
      </g>
      <!-- QA: gear and tick -->
      <g transform="translate(596 379)">
        <circle cx="-8" cy="-6" r="9" stroke-dasharray="4 2.5"/>
        <circle cx="-8" cy="-6" r="4"/>
        <circle cx="9" cy="5" r="9"/>
        <path d="M5 5 L8 8 L13 2"/>
        <path d="M4 13 L1 22 L5 20 L7 24 M14 13 L17 22 L13 20 L11 24"/>
      </g>
      <!-- monitoring: screen chart -->
      <g transform="translate(801 503)">
        <rect x="-22" y="-16" width="36" height="26" rx="2"/>
        <path d="M-4 10 V16 M-12 18 H4"/>
        <path d="M-15 4 V-2 M-10 4 V-6 M-5 4 V-4 M0 4 V-9"/>
        <circle cx="12" cy="-6" r="7"/>
        <path d="M17 -1 L23 6"/>
      </g>
      <!-- renewal: document, arrows, house -->
      <g transform="translate(907 293)">
        <rect x="-20" y="-22" width="16" height="20" rx="1"/>
        <path d="M-16 -16 H-8 M-16 -11 H-8 M-16 -6 H-8"/>
        <path d="M2 -18 H8 V-6 M5 -9 L8 -6 L11 -9"/>
        <path d="M-10 12 H-16 V0 M-19 3 L-16 0 L-13 3"/>
        <path d="M0 8 L10 0 L20 8 M3 6 V20 H17 V6 M8 20 V13 H12 V20"/>
      </g>
      <!-- guarantee: award badge -->
      <g transform="translate(722 182)">
        <circle cx="0" cy="-6" r="15" stroke-dasharray="5 2.5"/>
        <circle cx="0" cy="-6" r="9"/>
        <path d="M-4 -6 L-1 -3 L5 -10"/>
        <path d="M-9 7 L-13 22 L-7 19 L-4 24 L0 10 L4 24 L7 19 L13 22 L9 7"/>
      </g>
    </g>
  </svg>

  <h1 class="process__title">Unique Process</h1>

  <section class="step" style="left:559px; top:89px;">
    <h2 class="step__name">Step 7 - Halvern Guarantee</h2>
    <p>Sleep Easy! You’ll never fall<br>“out of contract” with Halvern<br>as your broker</p>
  </section>

  <section class="step" style="left:428px; top:268px;">
    <h2 class="step__name">Step 4 - Halvern QA</h2>
    <p>Every order detail is confirmed<br>to ensure accuracy and<br>smooth processing.</p>
  </section>

  <section class="step" style="left:130px; top:303px;">
    <h2 class="step__name">Step 2 - Halvern options!</h2>
    <p>We’ll send you an energy quote<br>with at least three options to<br>choose from - including<br>different suppliers and contract<br>terms. Our unbiased advice will<br>help you find the best solution!</p>
  </section>

  <section class="step" style="left:1031px; top:357px;">
    <h2 class="step__name">Step 6 - Halvern Renewal</h2>
    <p>To protect your business from<br>market volatility, we contact you<br>ahead of your contract end date to<br>discuss renewal options. If anyone else<br>contacts you, you respond,<br>“No thank you, we have Halvern!”</p>
  </section>

  <section class="step" style="left:955px; top:566px;">
    <h2 class="step__name">Step 5 - Halvern Monitoring</h2>
    <p>We proactively monitor your accounts<br>to address any contractual issues<br>with suppliers, should they arise.<br>(E.g., You sell your business,<br>account number changes, etc.)</p>
  </section>

  <section class="step" style="left:608px; top:653px;">
    <h2 class="step__name">Step 3 - Halvern sign-up!</h2>
    <p>Our simple sign-up process is<br>handled electronically.<br>Even contract signatures.</p>
  </section>

  <section class="step" style="left:301px; top:710px;">
    <h2 class="step__name">Step 1 - Halvern Assessment</h2>
    <p>Spend 15 minutes with our team<br>while we analyze your account<br>and contract details to select<br>suppliers that fit your needs.</p>
  </section>

  <div class="brand">
    <span class="brand__square"></span>
    <span class="brand__name">HALVERN POWER</span>
  </div>
</main>
</body>
</html>
```